Maple Ridge business card design

Card needs to include the following text/items:
Company Logo
Tobin Marsh
Phone # - 555-318-7642
service@mapleridgelandscaping.example
Lawn & landscape maintenance services

```html
<!DOCTYPE html>
<html lang="en">
<head>
<meta charset="utf-8">
<title>Maple Ridge Landscaping – Business Card</title>
<link rel="stylesheet" href="https://fonts.googleapis.com/css2?family=Cinzel:wght@700&family=EB+Garamond:wght@400;500&display=swap">
<style>
  :root {
    --backdrop: #2b2c2e;
    --forest: #1f4a2a;
    --leaf: #2f6b35;
    --olive: #7b8f2a;
    --amber: #f0a830;
    --ink: #3a3a3a;
    --paper-light: #ffffff;
    --paper-shade: #e6e7e8;
  }
  * { box-sizing: border-box; margin: 0; padding: 0; }
  html, body {
    width: 1200px; height: 900px; overflow: hidden;
    background: var(--backdrop);
  }
  .canvas { position: relative; width: 1200px; height: 900px; }

  .card {
    position: absolute;
    width: 580px; height: 332px;
    background: var(--forest);
    padding: 14px;
    box-shadow: 0 10px 24px rgba(0,0,0,.45);
  }
  .card--front { left: 90px; top: 80px; }
  .card--back  { left: 530px; top: 488px; }

  .card__face {
    position: relative; width: 100%; height: 100%;
    background: linear-gradient(120deg, var(--paper-shade) 0%, var(--paper-light) 55%, var(--paper-shade) 100%);
  }

  .brand { display: flex; align-items: center; gap: 14px; }
  .brand__dot {
    width: 44px; height: 44px; border-radius: 50%;
    background: var(--leaf);
    flex: none;
  }
  .brand__name {
    font-family: "Cinzel", serif; font-weight: 700;
    color: var(--forest); line-height: 1.05;
    letter-spacing: .5px;
  }

  /* front */
  .card--front .brand {
    position: absolute; left: 0; right: 0; top: 96px;
    justify-content: center;
  }
  .card--front .brand__name { font-size: 30px; }
  .front__rule {
    position: absolute; left: 70px; right: 70px; top: 196px;
    height: 1px; background: var(--olive);
  }
  .front__tagline {
    position: absolute; left: 0; right: 0; top: 208px;
    text-align: center;
    font-family: "EB Garamond", serif; font-weight: 500;
    font-size: 20px; color: var(--forest);
  }

  /* back */
  .card--back .brand {
    position: absolute; right: 30px; top: 60px;
    flex-direction: column; align-items: flex-end; gap: 10px;
  }
  .card--back .brand__dot { width: 64px; height: 64px; }
  .card--back .brand__name { font-size: 32px; text-align: right; }
  .contact__name {
    position: absolute; left: 34px; top: 196px;
    font-family: "Cinzel", serif; font-weight: 700;
    font-size: 22px; color: var(--olive); letter-spacing: .5px;
  }
  .contact__rule {
    position: absolute; left: 34px; right: 30px; top: 232px;
    height: 1px; background: var(--amber);
  }
  .contact__list {
    position: absolute; left: 34px; right: 20px; top: 246px;
    display: flex; gap: 26px; list-style: none;
    font-family: "EB Garamond", serif; font-size: 17px; color: var(--ink);
  }
  .contact__item { display: flex; align-items: center; gap: 7px; white-space: nowrap; }
  .contact__icon { width: 15px; height: 15px; fill: var(--leaf); flex: none; }
</style>
</head>
<body>
<main class="canvas">

  <section class="card card--front" aria-label="Business card front">
    <div class="card__face">
      <div class="brand">
        <span class="brand__dot"></span>
        <span class="brand__name">Maple Ridge<br>Landscaping</span>
      </div>
      <div class="front__rule"></div>
      <p class="front__tagline">Lawn &amp; landscape maintenance services</p>
    </div>
  </section>

  <section class="card card--back" aria-label="Business card back">
    <div class="card__face">
      <div class="brand">
        <span class="brand__dot"></span>
        <span class="brand__name">Maple Ridge<br>Landscaping</span>
      </div>
      <p class="contact__name">TOBIN MARSH</p>
      <div class="contact__rule"></div>
      <ul class="contact__list">
        <li class="contact__item">
          <svg class="contact__icon" viewBox="0 0 24 24" aria-hidden="true"><path d="M6.6 10.8a15.1 15.1 0 0 0 6.6 6.6l2.2-2.2a1 1 0 0 1 1-.25 11.4 11.4 0 0 0 3.6.57 1 1 0 0 1 1 1V20a1 1 0 0 1-1 1A17 17 0 0 1 3 4a1 1 0 0 1 1-1h3.5a1 1 0 0 1 1 1c0 1.25.2 2.45.57 3.57a1 1 0 0 1-.25 1z"/></svg>
          555-318-7642
        </li>
        <li class="contact__item">
          <svg class="contact__icon" viewBox="0 0 24 24" aria-hidden="true"><path d="M3 5h18a1 1 0 0 1 1 1v12a1 1 0 0 1-1 1H3a1 1 0 0 1-1-1V6a1 1 0 0 1 1-1zm9 7.2L4.2 7H4v.6l8 5.3 8-5.3V7h-.2z"/></svg>
          service@mapleridgelandscaping.example
        </li>
      </ul>
    </div>
  </section>

</main>
</body>
</html>
```